Website for UK Fintech Company specialising in Auto-Finance asset management

We need a website for a FINTECH business called KELVO Asset Management. We have developed and licenced an innovative platform to provide financial institutions whom provide secured Asset finance loans to consumer and commercial clients, allowing for real time tracking and management of defaulted accounts pending repossession. The KELVO Asset Management platform is a total recoveries solution through the cycle, from the moment the lender has to recover the vehicle (due to default/non-payment) to the disposal of the vehicle (via sale at Motor Auctions or by selling to a Car dealership network). The data provided from external services allows the Financier to make informed decisions, such as whether it is economical to continue the recovery and decide which sales channel is better suited for their assets to maximise residual values and minimise financial losses. The KELVO platform provides an array of MI reporting and uses a systematic approach utilising exception reporting to identify key areas of non-performance to enable focus where needed. KELVO also provides a leading Debt collection service recovering end-of-cycle losses such as Financial Shortfall and losses in vehicle values due to conditions and excessive damage.

We also require a new logo for out new product called PL-Certify

Target Market(s)

Financial institutions whom provide secured Asset finance loans to consumer and commercial clients

Industry/Entity Type

Financial Service

Logo Text

PL- Certify (this is for a new product which forms part of the KELVO Asset Mangement Platform

Number of Pages Required

4 page

Font styles to use
Serif
Sans Serif

Colors

Designer to choose colors to be used in the design.

Requirements
Must have
• We need a simple website with a broken down as follows;
• • Landing page
• • Services page
• • About us page
• • KELVO Asset Management Platform login page (client facing)
Nice to have
• Our slogan is 'Auto-Finance Expertise'
• We are very much open to suggestions as long as we can create a professional/ corporate / modern feel to the website. We are a FINTECH company, and that needs to come across
Should not have
• Whilst we are an asset management company primarily managing vehicles through our platform, we don't want it to look like a car dealership website!:)

```html
<!DOCTYPE html>
<html lang="en">
<head>
<meta charset="utf-8">
<title>PL-Certify</title>
<link rel="stylesheet" href="https://fonts.googleapis.com/css2?family=Anton&family=Lato:wght@400;700&display=swap">
<style>
  :root {
    --orange: #f7a800;
    --orange-soft: #f8c94a;
    --pink: #d9457a;
    --ink: #3c3c3c;
    --muted: #8a8a8a;
    --line: #c9c9c9;
    --white: #ffffff;
    --nav-bg: rgba(10, 10, 10, 0.82);
    --panel-bg: rgba(28, 28, 28, 0.86);
    --footer-bg: #2b3020;
  }
  * { margin: 0; padding: 0; box-sizing: border-box; }
  html, body { width: 1200px; height: 2594px; overflow: hidden; }
  body { position: relative; font-family: "Lato", Arial, sans-serif; color: var(--ink); background: var(--white); }
  .abs { position: absolute; }
  .display { font-family: "Anton", "Impact", sans-serif; font-weight: 400; letter-spacing: 0.5px; }
  .btn { position: absolute; display: flex; align-items: center; justify-content: center; background: var(--orange); color: var(--white); font-weight: 700; font-size: 16px; }

  /* Header */
  .site-header { position: absolute; left: 0; top: 0; width: 1200px; height: 71px; background: var(--nav-bg); z-index: 2; }
  .brand { position: absolute; left: 84px; top: 20px; display: flex; align-items: center; gap: 9px; color: var(--white); font-weight: 700; font-size: 21px; }
  .brand-dot { width: 13px; height: 13px; border-radius: 50%; background: var(--white); }
  .nav-item { position: absolute; top: 0; height: 52px; display: flex; align-items: center; justify-content: center; color: var(--white); font-weight: 700; font-size: 14px; }
  .nav-item.active { background: var(--orange); border-bottom: 4px solid var(--pink); }
  .login { position: absolute; left: 994px; top: 14px; width: 119px; height: 27px; background: var(--orange); color: var(--white); font-weight: 700; font-size: 14px; display: flex; align-items: center; justify-content: center; border-radius: 2px; }

  /* Hero */
  .hero { position: absolute; left: 0; top: 0; width: 1200px; height: 598px; overflow: hidden;
    background:
      radial-gradient(ellipse 260px 300px at 900px 300px, rgba(214,150,110,0.85), rgba(214,150,110,0) 70%),
      radial-gradient(ellipse 200px 170px at 1040px 160px, rgba(230,180,120,0.8), rgba(230,180,120,0) 70%),
      radial-gradient(ellipse 160px 160px at 1130px 80px, rgba(240,220,150,0.75), rgba(240,220,150,0) 70%),
      linear-gradient(180deg, rgba(0,0,0,0) 0%, rgba(0,0,0,0) 70%, rgba(120,140,40,0.75) 88%, rgba(70,90,20,0.9) 100%),
      linear-gradient(95deg, #0f130b 0%, #1a2410 35%, #2c3a18 55%, #55562a 72%, #7a6a38 88%, #3f4d1c 100%); }
  .hero-title { left: 86px; top: 248px; font-size: 55px; line-height: 70px; color: var(--white); text-shadow: 0 2px 6px rgba(0,0,0,0.5); }
  .hero .btn { left: 86px; top: 417px; width: 201px; height: 50px; }

  /* About */
  .about { position: absolute; left: 0; top: 598px; width: 1200px; height: 515px; }
  .section-title { color: var(--orange); font-size: 46px; text-align: center; }
  .about .section-title { left: 86px; top: 42px; width: 502px; }
  .about-text { left: 88px; top: 120px; width: 498px; text-align: center; font-size: 14px; line-height: 21px; }
  .about-text p + p { margin-top: 10px; }
  .about .btn { left: 261px; top: 412px; width: 149px; height: 50px; }
  .photo-frame { position: absolute; border: 3px solid var(--white); box-shadow: 0 2px 8px rgba(0,0,0,0.35); }
  .photo-a { left: 612px; top: 52px; width: 353px; height: 225px; z-index: 1;
    background: radial-gradient(ellipse 90px 110px at 130px 120px, rgba(200,170,150,0.8), rgba(200,170,150,0) 70%),
                linear-gradient(120deg, #eef2f5 0%, #c9d1d6 45%, #6f767c 75%, #3e4246 100%); }
  .photo-b { left: 787px; top: 156px; width: 326px; height: 278px;
    background: linear-gradient(180deg, rgba(0,0,0,0) 30%, rgba(60,40,25,0.6) 100%),
                repeating-linear-gradient(90deg, #8e6e50 0 50px, #b89a72 50px 70px, #7a5c42 70px 110px),
                linear-gradient(160deg, #c9a88e, #5a4030); }

  /* Services */
  .services { position: absolute; left: 0; top: 1113px; width: 1200px; height: 554px; overflow: hidden;
    background:
      radial-gradient(ellipse 180px 120px at 390px 190px, rgba(245,248,250,0.95), rgba(200,208,215,0.6) 55%, rgba(200,208,215,0) 75%),
      radial-gradient(ellipse 260px 160px at 400px 260px, rgba(150,160,170,0.7), rgba(150,160,170,0) 70%),
      repeating-linear-gradient(160deg, rgba(90,120,150,0.25) 0 40px, rgba(200,180,150,0.25) 40px 90px, rgba(220,110,60,0.15) 90px 110px),
      linear-gradient(120deg, #a9b6c2 0%, #6d7e8e 40%, #c4b49c 65%, #5b6c7c 100%); }
  .services-panel { left: 612px; top: 54px; width: 501px; height: 446px; background: var(--panel-bg); color: var(--white); }
  .services-panel .section-title { color: var(--white); position: static; margin-top: 42px; }
  .services-panel p { width: 380px; margin: 16px auto 0; text-align: center; font-size: 13px; line-height: 21px; }
  .thumb { position: absolute; top: 351px; width: 86px; height: 86px; border-radius: 50%; }
  .thumb.t1 { left: 85px; background: radial-gradient(circle, #e2e6ea, #8c959e); }
  .thumb.t2 { left: 208px; top: 346px; width: 96px; height: 96px; background: radial-gradient(circle, #d8b48c, #8b6a45); border: 4px solid var(--orange-soft); }
  .thumb.t3 { left: 325px; background: radial-gradient(circle, #d9e6ee, #6e9ab8); }
  .slider-arrow { position: absolute; top: 382px; }

  /* Testimonial */
  .testimonial { position: absolute; left: 0; top: 1667px; width: 1200px; height: 439px; border-bottom: 1px solid #e3e3e3; }
  .testimonial .section-title { left: 0; top: 42px; width: 1200px; }
  .quote-frame { left: 147px; top: 173px; width: 906px; height: 179px; border: 3px solid var(--orange-soft); }
  .portrait { left: 173px; top: 128px; width: 237px; height: 261px; background: linear-gradient(160deg, #4a3226 0%, #7b5a44 30%, #c79a80 55%, #d4588f 100%); }
  .quote-badge { left: 387px; top: 124px; width: 66px; height: 66px; border-radius: 50%; background: var(--orange-soft); border: 3px solid var(--white); display: flex; align-items: center; justify-content: center; color: var(--white); font-family: Georgia, serif; font-size: 54px; line-height: 1; padding-top: 18px; }
  .quote-text { left: 437px; top: 197px; width: 590px; font-size: 13px; line-height: 21px; color: #555; }
  .attribution { left: 437px; top: 373px; display: flex; align-items: center; gap: 10px; font-size: 12.5px; color: var(--muted); }
  .attribution .rule { width: 108px; height: 1px; background: var(--orange-soft); }
  .pager { position: absolute; top: 373px; width: 16px; height: 15px; display: flex; align-items: center; justify-content: center; }
  .pager.prev { left: 1020px; background: var(--orange-soft); }
  .pager.next { left: 1039px; background: #cfcfcf; }

  /* Contact */
  .contact { position: absolute; left: 0; top: 2107px; width: 1200px; height: 414px; background: linear-gradient(135deg, #fbfbfb 0%, #f1f1f1 40%, #fafafa 70%, #efefef 100%); }
  .contact .section-title { left: 0; top: 40px; width: 1200px; font-size: 44px; line-height: 60px; }
  .contact-sub { left: 0; top: 104px; width: 1200px; text-align: center; font-size: 15px; color: var(--muted); }
  .field { position: absolute; border-bottom: 1px solid var(--line); font-size: 14px; color: #a3a3a3; padding-bottom: 5px; }
  .contact .btn { left: 526px; top: 310px; width: 148px; height: 50px; }

  /* Footer */
  .site-footer { position: absolute; left: 0; top: 2521px; width: 1200px; height: 73px; background: var(--footer-bg); color: var(--white); }
  .social { position: absolute; left: 458px; top: 16px; display: flex; gap: 28px; }
  .social span { width: 16px; height: 16px; border-radius: 3px; border: 2px solid var(--white); display: block; }
  .copyright { position: absolute; left: 0; top: 48px; width: 1200px; text-align: center; font-size: 12px; letter-spacing: 0.4px; }
</style>
</head>
<body>

<section class="hero">
  <div class="abs" style="left:0;top:0;width:1200px;height:598px" role="img" aria-label="Family smiling together outdoors on a sunny lawn"></div>
  <h1 class="abs display hero-title">Lorem Ipsum is simply<br>dummy text of the printing</h1>
  <a class="btn">Read More</a>
</section>

<header class="site-header">
  <div class="brand"><span class="brand-dot"></span>PL-Certify</div>
  <nav>
    <a class="nav-item active" style="left:491px;width:76px">Home</a>
    <a class="nav-item" style="left:600px;width:90px">About Us</a>
    <a class="nav-item" style="left:721px;width:90px">Service</a>
    <a class="nav-item" style="left:842px;width:100px">Contact Us</a>
  </nav>
  <a class="login">Log In</a>
</header>

<section class="about">
  <h2 class="abs display section-title">About Us</h2>
  <div class="abs about-text">
    <p>Lorem Ipsum is simply dummy text of the printing and typesetting industry. Lorem Ipsum has been the industry's standard dummy text ever since the 1500s, when an unknown printer took a galley of type and scrambled it to make a type specimen book. It has survived not only five centuries, but also the leap into electronic typesetting, remaining essentially unchanged. It was popularised in the 1960s</p>
    <p>Lorem Ipsum is simply dummy text of the printing and typesetting industry. Lorem Ipsum has been the industry's standard dummy text ever since the 1500s, when an unknown printer took a galley of type and scrambled it to make a type specimen book. It has survived not only five centuries, but also the leap into electronic typesetting, remaining essentially unchanged. It was popularised in the 1960s</p>
  </div>
  <a class="btn">Read More</a>
  <div class="photo-frame photo-a" role="img" aria-label="Couple meeting an adviser to sign finance papers"></div>
  <div class="photo-frame photo-b" role="img" aria-label="Stacks of coins on a table"></div>
</section>

<section class="services">
  <div class="abs" style="left:0;top:0;width:1200px;height:554px" role="img" aria-label="Stethoscope resting on banknotes"></div>
  <div class="abs services-panel">
    <h2 class="display section-title">Our Services</h2>
    <p>Lorem Ipsum is simply dummy text of the printing and typesetting industry. Lorem Ipsum has been the industry's standard dummy text ever since the 1500s, when an unknown printer took a galley of type and scrambled it to make a type specimen book. It has survived not only five centuries, but also the leap into electronic typesetting, remaining essentially unchanged. It was popularised in the 1960s!</p>
    <svg class="slider-arrow" style="left:22px" width="16" height="26" viewBox="0 0 16 26"><path d="M13 3 L4 13 L13 23" fill="none" stroke="#fff" stroke-width="3"/></svg>
    <div class="thumb t1" role="img" aria-label="Service thumbnail: stethoscope"></div>
    <div class="thumb t2" role="img" aria-label="Service thumbnail: family"></div>
    <div class="thumb t3" role="img" aria-label="Service thumbnail: hand with icons"></div>
    <svg class="slider-arrow" style="left:463px" width="16" height="26" viewBox="0 0 16 26"><path d="M3 3 L12 13 L3 23" fill="none" stroke="#fff" stroke-width="3"/></svg>
  </div>
</section>

<section class="testimonial">
  <h2 class="abs display section-title">Testimonial</h2>
  <div class="abs quote-frame"></div>
  <div class="abs portrait" role="img" aria-label="Portrait of a smiling client"></div>
  <div class="abs quote-badge">&ldquo;</div>
  <p class="abs quote-text">Lorem Ipsum is simply dummy text of the printing and typesetting industry. Lorem Ipsum has been the industry's standard dummy text ever since the 1500s, when an unknown printer took a galley of type and scrambled it to make a Lorem Ipsum is simply dummy text of the printing and typesetting industry. Lorem Ipsum has been the industry's standard dummy text ever since the 1500s, when an unknown printer took a galley of type and scrambled it to make.</p>
  <div class="abs attribution"><span class="rule"></span><span>Mara Hollin &nbsp;|&nbsp; Lorem ipsum</span></div>
  <span class="pager prev"><svg width="6" height="8" viewBox="0 0 6 8"><path d="M5 0 L0 4 L5 8Z" fill="#fff"/></svg></span>
  <span class="pager next"><svg width="6" height="8" viewBox="0 0 6 8"><path d="M1 0 L6 4 L1 8Z" fill="#fff"/></svg></span>
</section>

<section class="contact">
  <h2 class="abs display section-title">CONTACT US</h2>
  <p class="abs contact-sub">Lorem ipsum dolor sit amet, consectetur adipiscing elit.</p>
  <div class="field" style="left:107px;top:153px;width:464px">Name</div>
  <div class="field" style="left:107px;top:205px;width:464px">Email</div>
  <div class="field" style="left:107px;top:258px;width:464px">Phone No</div>
  <div class="field" style="left:629px;top:153px;width:464px;height:129px">Message</div>
  <a class="btn">Send Message</a>
</section>

<footer class="site-footer">
  <div class="social" aria-label="Social links">
    <span></span><span></span><span></span><span></span><span></span><span></span><span></span>
  </div>
  <p class="copyright">© 2017 pl certify. All Rights Reserved.</p>
</footer>

</body>
</html>
```